Velno Recycling needs a new web design

We need a new web design for our company based in Austin, TX. We resell and recycling electronics such as laptops, computer components, Tovlets, Brunos, etc. Since our inception over ten years ago, we’ve become one of the premier electronics recycling and remarketing companies in Austin, Texas.

```html
<!DOCTYPE html>
<html lang="en">
<head>
<meta charset="utf-8">
<title>Velno Recycling</title>
<link href="https://fonts.googleapis.com/css2?family=Poppins:wght@400;500;600;700&family=Open+Sans:ital,wght@0,400;0,600;0,700;1,400&display=swap" rel="stylesheet">
<style>
:root{
  --blue:#1b6fbd;
  --blue-dark:#135a9e;
  --ink:#222;
  --text:#555;
  --muted:#888;
  --light:#f3f3f3;
  --grey-band:#e9e9e9;
  --navy:#1f3a5c;
  --footer:#1c1c1c;
  --footer-line:#333;
  --white:#fff;
}
*{margin:0;padding:0;box-sizing:border-box}
html,body{width:1200px;height:2695px;overflow:hidden}
body{font-family:"Open Sans",Arial,sans-serif;color:var(--text);background:var(--white);position:relative}
.abs{position:absolute}
h1,h2,h3,h4{font-family:"Poppins",Arial,sans-serif;color:var(--ink)}
.btn{display:inline-flex;align-items:center;justify-content:center;background:var(--blue);color:var(--white);font-family:"Poppins",sans-serif;font-size:12px;font-weight:500;border-radius:16px;height:28px}

/* header */
.topbar{left:0;top:0;width:1200px;height:33px;background:var(--white)}
.topbar-contact{right:190px;top:8px;font-size:11px;color:#333;display:flex;gap:18px;align-items:center}
.dot{width:10px;height:10px;border-radius:50%;background:#666;display:block}
.navbar{left:0;top:33px;width:1200px;height:46px;background:var(--blue)}
.brand-box{left:210px;top:0;width:166px;height:86px;background:var(--white);box-shadow:0 2px 6px rgba(0,0,0,.15);display:flex;align-items:center;justify-content:center;gap:8px;z-index:2}
.brand-box .mark{width:26px;height:26px;border-radius:50%;background:var(--blue)}
.brand-box span{font-family:"Poppins",sans-serif;font-weight:600;font-size:15px;color:var(--blue);line-height:1.05}
.nav{left:441px;top:33px;height:46px;display:flex;align-items:center;gap:19px;font-size:11.5px;color:var(--white);font-family:"Poppins",sans-serif}
.nav .book{background:var(--white);color:var(--blue-dark);border-radius:14px;padding:6px 16px;font-weight:600;margin-left:10px}

/* hero */
.hero{left:0;top:79px;width:1200px;height:467px;background:linear-gradient(180deg,#f4f5f6,#e8eaec)}
.hero-photo{left:593px;top:0;width:607px;height:467px;background:linear-gradient(135deg,#cfd4d8 0%,#8a8f93 40%,#2b2d30 60%,#3f8a3a 85%,#2f6d2b 100%)}
.hero-title{left:210px;top:107px;display:flex;align-items:center;gap:14px}
.hero-title .mark{width:54px;height:54px;border-radius:50%;background:var(--blue)}
.hero-title h1{font-size:28px;font-weight:600;line-height:1.2}
.hero-text{left:210px;top:199px;width:380px;font-size:11.5px;line-height:21px}
.hero .btn{left:210px;top:332px;width:113px}
.dots{left:210px;top:440px;display:flex;gap:3px}
.dots i{width:8px;height:8px;border-radius:50%;border:1px solid var(--blue);display:block}
.dots i:first-child{background:var(--blue)}

/* welcome */
.welcome{left:0;top:546px;width:1200px;height:377px;background:var(--white)}
.welcome-copy{left:210px;top:56px;width:300px}
.welcome-copy small{font-size:12px;color:#444}
.welcome-copy h2{font-size:24px;font-weight:600;margin-bottom:16px;line-height:1.2}
.welcome-copy p{font-size:11px;line-height:20px;margin-bottom:16px}
.welcome-copy .btn{width:113px}
.service{top:54px;width:212px;text-align:center}
.service .photo{height:160px;width:212px}
.service .icon{width:36px;height:36px;border-radius:50%;background:var(--blue);margin:-18px auto 0;position:relative;border:3px solid var(--white)}
.service h3{font-size:14px;font-weight:500;margin:12px 0 14px}
.service p{font-size:11px;line-height:19px;padding:0 10px}

/* products */
.products{left:0;top:923px;width:1200px;height:340px;background:linear-gradient(135deg,#1d3d66,#2c5a8a 50%,#1c3a5f)}
.products h2{left:0;width:1200px;top:50px;text-align:center;color:var(--white);font-size:22px;font-weight:600}
.product-row{left:210px;top:99px;display:flex;gap:9.6px}
.product{width:122px;height:129px;background:var(--white);border-radius:4px;text-align:center;padding-top:16px}
.product .ring{width:56px;height:56px;border-radius:50%;border:4px solid #eee;margin:0 auto 14px;display:flex;align-items:center;justify-content:center}
.product h4{font-size:12px;font-weight:500}
.product span{font-size:10px;color:var(--muted)}
.products .btn{left:531px;top:255px;width:138px;border:1px solid var(--white)}

/* certified */
.certified{left:0;top:1263px;width:1200px;height:465px;background:var(--grey-band)}
.certified h2{left:0;width:1200px;top:48px;text-align:center;font-size:25px;font-weight:600}
.certified p{left:350px;width:500px;top:91px;text-align:center;font-size:11px;line-height:20px}
.cert-row{left:210px;top:147px;display:flex;gap:8px}
.cert{width:189px;height:266px;border:3px solid #2e7d4f;background:linear-gradient(180deg,#e4efe3,#cfe2cf);display:flex;align-items:flex-end;justify-content:center;padding-bottom:24px}
.cert .seal{width:30px;height:30px;border-radius:50%;background:#c9a646}
.cert.plain{background:var(--white);border-color:#1c3a5f}

/* why & testimonials */
.why{left:0;top:1728px;width:1200px;height:384px;background:var(--white)}
.why h2{font-size:23px;font-weight:600}
.why-title{left:210px;top:52px}
.benefit{width:240px;display:flex;gap:12px}
.benefit svg{flex:none;margin-top:2px}
.benefit h4{font-family:"Open Sans",sans-serif;font-size:12.5px;font-weight:600;color:#333;margin-bottom:6px}
.benefit p{font-size:11px;line-height:18px;color:var(--muted)}
.testi-title{left:744px;top:52px}
.testimonial{left:744px;top:113px;width:246px;height:201px;border:2px solid var(--blue);border-radius:4px;overflow:hidden}
.testimonial blockquote{padding:20px 8px 0 22px;font-style:italic;font-size:10.5px;line-height:19px;color:#444;white-space:nowrap;height:153px}
.testi-bar{position:absolute;left:0;bottom:0;width:100%;height:46px;background:var(--blue);color:var(--white);display:flex;align-items:center;justify-content:space-between;padding:0 22px 0 38px}
.testi-bar b{font-style:italic;font-size:13px;font-weight:600;display:block}
.stars{color:#f5c518;font-size:11px;letter-spacing:1px}

/* cta */
.cta{left:0;top:2112px;width:1200px;height:180px;background:linear-gradient(135deg,#1c3a5f,#2d5c8b 50%,#1a3758)}
.cta h2{left:0;width:1200px;top:47px;text-align:center;color:var(--white);font-size:22px;font-weight:600}
.cta .btn{left:531px;top:99px;width:138px;border:1px solid var(--white)}

/* footer */
.footer{left:0;top:2292px;width:1200px;height:403px;background:var(--footer);color:#bbb}
.footer-brand{left:210px;top:40px;display:flex;align-items:center;gap:12px}
.footer-brand .mark{width:60px;height:60px;border-radius:50%;border:3px solid var(--white)}
.footer-brand span{font-family:"Poppins",sans-serif;font-weight:500;font-size:28px;color:var(--white);line-height:1}
.footer h4{color:var(--white);font-size:13px;font-weight:600;margin-bottom:12px}
.footer-info{left:210px;top:143px;font-size:11px;line-height:19px}
.footer-social{display:flex;gap:14px;margin-top:12px}
.footer-social .dot{background:#aaa}
.footer-nav{left:410px;top:143px;font-size:11px;line-height:18.5px}
.footer-divider{left:545px;top:36px;width:1px;height:300px;background:var(--footer-line)}
.contact{left:610px;top:39px;width:380px}
.field{background:var(--white);height:29px;border-radius:2px;font-size:10px;color:#aaa;padding:8px 10px;margin-bottom:9px}
.pair{display:flex;gap:6px}
.pair .field{flex:1}
.field.msg{height:71px}
.submit{width:94px;height:29px;background:var(--blue);color:var(--white);font-size:11px;display:flex;align-items:center;justify-content:center;border-radius:2px;margin-top:5px}
.footer-bottom{left:210px;top:361px;width:780px;display:flex;justify-content:space-between;font-size:10px;color:#aaa}
.footer-bottom nav{display:flex;gap:14px}
</style>
</head>
<body>

<header>
  <div class="abs topbar"></div>
  <div class="abs topbar-contact">
    <span>&#9742; (512) 555-0148</span>
    <span>&#9993; hello@velnorecycling.com</span>
    <span style="display:flex;gap:14px"><i class="dot"></i><i class="dot"></i><i class="dot"></i></span>
  </div>
  <div class="abs navbar"></div>
  <div class="abs brand-box"><i class="mark"></i><span>Velno<br>Recycling</span></div>
  <nav class="abs nav">
    <span>Home</span><span>About</span><span>Services</span><span>Certifications</span><span>Testimonials</span><span>Events</span><span>Contact</span><span class="book">Book Online</span>
  </nav>
</header>

<section class="abs hero">
  <div class="abs hero-photo" role="img" aria-label="Person dropping a computer tower into a green recycling bin"></div>
  <div class="abs hero-title"><i class="mark"></i><h1>Computer Recycling<br>Made Easy</h1></div>
  <p class="abs hero-text">Want to make a difference to our environment and planet? Velno Recycling is here to help! Velno recycling has been helping keep the environment healthy since 2006, we specialize in recycling services that help citizens become experts at reducing waste. We have a passion to keep our world clean and are here to guide you through all the stages of the recycling process.</p>
  <span class="abs btn">Find Out More</span>
  <div class="abs dots"><i></i><i></i><i></i><i></i><i></i></div>
</section>

<section class="abs welcome">
  <div class="abs welcome-copy">
    <small>Welcome to</small>
    <h2>Velno Recycling</h2>
    <p>At Velno Recycling, we're committed to providing environmentally friendly recycling solutions to Austin and the surrounding areas.</p>
    <p>Founded in 2006, our mission is to process your materials in a safe, non-hazardous manner — with an aim to keep the world environmentally clean. As a R2 recycling center, we believe in promoting smart recycling habits in order to achieve long lasting results.</p>
    <span class="btn">Find Out More</span>
  </div>
  <article class="abs service" style="left:544px">
    <div class="photo" role="img" aria-label="Blue recycling bin filled with electronic waste on grass" style="background:linear-gradient(180deg,#b9c7d3,#3c6fb0 60%,#6a8f4a)"></div>
    <div class="icon"></div>
    <h3>Electronic Recycling</h3>
    <p>At Velno Recycling, we strive to keep the environment clean through our wide range of services.</p>
  </article>
  <article class="abs service" style="left:776px">
    <div class="photo" role="img" aria-label="Workers loading old appliances at a recycling pickup" style="background:linear-gradient(180deg,#c8ccd0,#8d9499 55%,#5e6469)"></div>
    <div class="icon"></div>
    <h3>Recycling Pickup</h3>
    <p>At Velno Recycling, we go out of our way to make sure your recycling process is made easy as possible.</p>
  </article>
</section>

<section class="abs products" role="img" aria-label="Blurred laptop keyboard background">
  <h2 class="abs">Resell and Recycling Products</h2>
  <div class="abs product-row">
    <div class="product"><div class="ring"><svg width="20" height="20" viewBox="0 0 20 20"><rect x="3" y="2" width="8" height="16" rx="1" fill="#1b6fbd"/><rect x="12" y="10" width="5" height="8" fill="#1b6fbd"/></svg></div><h4>Computers</h4><span>Recycling</span></div>
    <div class="product"><div class="ring"><svg width="20" height="20" viewBox="0 0 20 20"><rect x="2" y="3" width="16" height="11" rx="1" fill="none" stroke="#1b6fbd" stroke-width="2"/><rect x="7" y="15" width="6" height="2" fill="#1b6fbd"/></svg></div><h4>Brunos</h4><span>Recycling</span></div>
    <div class="product"><div class="ring"><svg width="20" height="20" viewBox="0 0 20 20"><rect x="4" y="4" width="12" height="9" fill="none" stroke="#1b6fbd" stroke-width="2"/><rect x="1" y="14" width="18" height="2" fill="#1b6fbd"/></svg></div><h4>Laptops</h4><span>Recycling</span></div>
    <div class="product"><div class="ring"><svg width="20" height="20" viewBox="0 0 20 20"><rect x="5" y="2" width="10" height="16" rx="2" fill="none" stroke="#1b6fbd" stroke-width="2"/></svg></div><h4>Tovlets</h4><span>Recycling</span></div>
    <div class="product"><div class="ring"><svg width="20" height="20" viewBox="0 0 20 20"><rect x="1" y="6" width="18" height="9" rx="1" fill="none" stroke="#1b6fbd" stroke-width="2"/><rect x="5" y="11" width="10" height="2" fill="#1b6fbd"/></svg></div><h4>Keyboard</h4><span>Recycling</span></div>
    <div class="product"><div class="ring"><svg width="20" height="20" viewBox="0 0 20 20"><rect x="2" y="5" width="10" height="8" fill="#1b6fbd"/><rect x="9" y="9" width="9" height="7" fill="none" stroke="#1b6fbd" stroke-width="2"/></svg></div><h4>All Component</h4><span>Recycling</span></div>
  </div>
  <span class="abs btn">Schedule A Pickup</span>
</section>

<section class="abs certified">
  <h2 class="abs">Certified Recyclers</h2>
  <p class="abs">Our inception over ten years ago, we've become one of the premier electronics recycling and remarketing companies in Austin, Texas.</p>
  <div class="abs cert-row">
    <div class="cert" role="img" aria-label="Certificate of registration"><i class="seal"></i></div>
    <div class="cert" role="img" aria-label="Certificate of registration"><i class="seal"></i></div>
    <div class="cert" role="img" aria-label="Certificate of registration"><i class="seal"></i></div>
    <div class="cert plain" role="img" aria-label="State environmental quality permit"></div>
  </div>
</section>

<section class="abs why">
  <h2 class="abs why-title">Why Choose Us</h2>
  <div class="abs benefit" style="left:210px;top:120px"><svg width="20" height="18" viewBox="0 0 20 18"><path d="M2 10l6 6L18 2" fill="none" stroke="#1b6fbd" stroke-width="3"/></svg><div><h4>Savings in time &amp; money</h4><p>Duis sed odio sit amet nibh vulputate cursus a sit amet.</p></div></div>
  <div class="abs benefit" style="left:476px;top:120px"><svg width="20" height="18" viewBox="0 0 20 18"><path d="M2 10l6 6L18 2" fill="none" stroke="#1b6fbd" stroke-width="3"/></svg><div><h4>Hassle-free service</h4><p>Duis sed odio sit amet nibh vulputate cursus a sit amet.</p></div></div>
  <div class="abs benefit" style="left:210px;top:201px"><svg width="20" height="18" viewBox="0 0 20 18"><path d="M2 10l6 6L18 2" fill="none" stroke="#1b6fbd" stroke-width="3"/></svg><div><h4>Multiple waste streams</h4><p>Duis sed odio sit amet nibh vulputate cursus a sit amet.</p></div></div>
  <div class="abs benefit" style="left:476px;top:201px"><svg width="20" height="18" viewBox="0 0 20 18"><path d="M2 10l6 6L18 2" fill="none" stroke="#1b6fbd" stroke-width="3"/></svg><div><h4>Recycle more of your waste</h4><p>Duis sed odio sit amet nibh vulputate cursus a sit amet.</p></div></div>
  <div class="abs benefit" style="left:210px;top:282px"><svg width="20" height="18" viewBox="0 0 20 18"><path d="M2 10l6 6L18 2" fill="none" stroke="#1b6fbd" stroke-width="3"/></svg><div><h4>Guaranteed peace of mind</h4><p>Duis sed odio sit amet nibh vulputate cursus a sit amet.</p></div></div>
  <div class="abs benefit" style="left:476px;top:282px"><svg width="20" height="18" viewBox="0 0 20 18"><path d="M2 10l6 6L18 2" fill="none" stroke="#1b6fbd" stroke-width="3"/></svg><div><h4>Social Responsibility</h4><p>Duis sed odio sit amet nibh vulputate cursus a sit amet.</p></div></div>

  <h2 class="abs testi-title">Testimonials</h2>
  <div class="abs testimonial">
    <blockquote>"Nullam ac urna eu felis dapibus<br>condimentum sit amet a augue. Sed<br>non neque elit. Sed ut imperdiet nisi.<br>Proin condimentum fermentum nunc.<br>Etiam pharetra, erat sed fermentum<br>velit mauris egestas quam."</blockquote>
    <div class="testi-bar"><div><b>- Marisol</b><span class="stars">&#9733;&#9733;&#9733;&#9733;&#9733;</span></div><svg width="24" height="12" viewBox="0 0 24 12"><path d="M6 1L1 6l5 5M18 1l5 5-5 5" fill="none" stroke="#fff" stroke-width="1.6"/></svg></div>
  </div>
</section>

<section class="abs cta" role="img" aria-label="Blurred computer hardware background">
  <h2 class="abs">Ready to get started? Call Us Today</h2>
  <span class="abs btn">Request Service</span>
</section>

<footer class="abs footer">
  <div class="abs footer-brand"><i class="mark"></i><span>Velno Recycling</span></div>
  <div class="abs footer-info">
    <h4>Contact Information</h4>
    <p>4210 Larkin Mill Rd<br>Austin TX USA 78757</p>
    <p style="margin-top:10px">(512) 555-0148<br>hello@velnorecycling.com</p>
    <div class="footer-social"><i class="dot"></i><i class="dot"></i><i class="dot"></i></div>
  </div>
  <div class="abs footer-nav">
    <h4>Navigation</h4>
    <p>Home<br>About<br>Services<br>Certifications<br>Testimonials<br>Events<br>Contact</p>
  </div>
  <div class="abs footer-divider"></div>
  <div class="abs contact">
    <h4>Contact Us</h4>
    <div class="pair"><div class="field">Name</div><div class="field">Email</div></div>
    <div class="pair"><div class="field">Phone</div><div class="field">Subject</div></div>
    <div class="field">Address</div>
    <div class="field msg">Message</div>
    <div class="submit">Submit</div>
  </div>
  <div class="abs footer-bottom">
    <span>©2018 by Velno Recycling. All Rights Reserved</span>
    <nav><span>Terms of Use</span><span>Privacy</span><span>Sitemap</span></nav>
  </div>
</footer>

</body>
</html>
```